Modern, profession Order Insert Card for Head Shop/Smoke shop

We are looking for a modern design for our Order Insert cards where we will have some text thanking the customer for their order.
The design needs to be professional and modern, showing our logo (SVG attached) and our website URL.
Our eCommerce store sells "head shop" items, things like bongs, rolling papers, cbd products, disposable vapes, etc.
I have uploaded 2 versions of our logo, one featuring the colour of green we use across our brand, a black logo or the logo can be inverted to be a white logo on a black background.
Target Market(s)
The websites target audience is anyone needing accessories or tools to consume medicinal marijuana/the consumers favourite herbs or any one in the vaping community.
Contact Information for Business Card
Website URL, Space for a small thank you note and our logo.
Look and feel

```html
<!DOCTYPE html>
<html lang="en">
<head>
<meta charset="utf-8">
<title>Greenhaven Goods – Order Insert Cards</title>
<link rel="stylesheet" href="https://fonts.googleapis.com/css2?family=Arimo:wght@400;700&display=swap">
<style>
  :root {
    --bg: #bdbdbd;
    --card: #f4f4f3;
    --green: #7dc242;
    --grey-band: #6f6f6f;
    --ink: #1c1c1c;
    --muted: #555555;
    --faint: #e9ecdf;
  }
  * { box-sizing: border-box; margin: 0; padding: 0; }
  html, body { width: 1200px; height: 900px; overflow: hidden; }
  body {
    background: var(--bg);
    font-family: "Arimo", Arial, sans-serif;
    color: var(--ink);
    position: relative;
  }
  .card {
    position: absolute;
    left: 320px;
    width: 560px;
    height: 320px;
    background: var(--card);
    overflow: hidden;
    box-shadow: 0 6px 18px rgba(0,0,0,.18);
  }
  .card--front { top: 90px; }
  .card--back { top: 470px; }

  .card__pattern {
    position: absolute;
    right: -30px;
    top: 90px;
    width: 260px;
    height: 230px;
    border-radius: 40% 30% 20% 40%;
    background: radial-gradient(ellipse at 55% 50%, var(--faint) 0%, rgba(233,236,223,0) 70%);
  }
  .card__swoosh { position: absolute; left: 0; bottom: 0; width: 560px; height: 320px; }
  .swoosh-grey { fill: var(--grey-band); }
  .swoosh-green { fill: var(--green); }

  .brand {
    display: flex;
    align-items: center;
    gap: 10px;
    font-weight: 700;
    font-size: 22px;
    letter-spacing: .5px;
    color: var(--ink);
    white-space: nowrap;
  }
  .brand__dot {
    width: 18px; height: 18px; border-radius: 50%;
    background: var(--green);
  }
  .card--front .brand {
    position: absolute;
    top: 110px;
    left: 0; right: 0;
    justify-content: center;
  }
  .tagline {
    position: absolute;
    top: 215px;
    left: 0; right: 0;
    text-align: center;
    font-size: 12px;
    color: var(--muted);
  }

  .card--back .brand { position: absolute; top: 34px; left: 56px; font-size: 19px; }
  .person { position: absolute; top: 82px; left: 44px; }
  .person__name { font-size: 21px; font-weight: 700; color: var(--green); }
  .person__role { font-size: 11px; color: var(--muted); margin-top: 3px; }
  .divider {
    position: absolute;
    top: 122px; left: 40px; right: 40px;
    border-top: 1px solid #8a8a8a;
  }
  .address {
    position: absolute;
    top: 132px; left: 40px;
    font-size: 11.5px;
    line-height: 1.45;
    color: var(--ink);
  }
  .contact-rule {
    position: absolute;
    top: 222px; left: 350px; right: 24px;
    border-top: 1px solid #8a8a8a;
  }
  .contact {
    position: absolute;
    right: 24px;
    top: 230px;
    list-style: none;
    text-align: right;
    font-size: 11.5px;
    line-height: 1.55;
  }
  .contact li { display: flex; justify-content: flex-end; align-items: center; gap: 6px; }
  .contact svg { width: 10px; height: 10px; fill: none; stroke: var(--ink); stroke-width: 1.6; }
  .thanks {
    position: absolute;
    left: 190px; bottom: 14px;
    color: #ffffff;
    font-size: 13px;
  }
</style>
</head>
<body>

  <section class="card card--front" aria-label="Order insert card, front">
    <div class="card__pattern" role="img" aria-label="Faint brand pattern area"></div>
    <div class="brand"><span class="brand__dot"></span>GREENHAVEN GOODS</div>
    <p class="tagline">Welcome to the best online smoke shop in the UK.</p>
    <svg class="card__swoosh" viewBox="0 0 560 320" aria-hidden="true">
      <path class="swoosh-grey" d="M0,258 Q260,272 560,308 L560,320 L0,320 Z"/>
      <path class="swoosh-green" d="M0,270 Q260,284 560,320 L0,320 Z"/>
    </svg>
  </section>

  <section class="card card--back" aria-label="Order insert card, back">
    <div class="card__pattern" role="img" aria-label="Faint brand pattern area"></div>
    <div class="brand"><span class="brand__dot"></span>GREENHAVEN GOODS</div>
    <div class="person">
      <p class="person__name">Your Name Here</p>
      <p class="person__role">President/Founder</p>
    </div>
    <div class="divider"></div>
    <p class="address">2727, Location, State Name<br>Siut 333,<br>Locate here, 3265</p>

    <svg class="card__swoosh" viewBox="0 0 560 320" aria-hidden="true">
      <path class="swoosh-grey" d="M0,178 Q150,190 250,250 Q360,312 560,312 L560,320 L0,320 Z"/>
      <path class="swoosh-green" d="M0,192 Q140,205 240,262 Q340,320 560,320 L0,320 Z"/>
    </svg>
    <p class="thanks">Thank you</p>

    <div class="contact-rule"></div>
    <ul class="contact">
      <li>(000) 111.2222 <svg viewBox="0 0 10 10"><path d="M2 1 L4 3 L3 4 Q4.5 6 6 7 L7 6 L9 8 L8 9 Q4 9 1 4 Z"/></svg></li>
      <li>(111) 222.3333 <svg viewBox="0 0 10 10"><path d="M2 1 L4 3 L3 4 Q4.5 6 6 7 L7 6 L9 8 L8 9 Q4 9 1 4 Z"/></svg></li>
      <li>hello@greenhavengoods.com <svg viewBox="0 0 10 10"><rect x="1" y="2" width="8" height="6"/><path d="M1 2 L5 5.5 L9 2"/></svg></li>
      <li>www.greenhavengoods.com <svg viewBox="0 0 10 10"><circle cx="5" cy="5" r="4"/><path d="M1 5 H9 M5 1 Q2.5 5 5 9 M5 1 Q7.5 5 5 9"/></svg></li>
    </ul>
  </section>

</body>
</html>
```